Bookkeeping website design

We need a basic site design for wordpress.
We are a bookkeeping business and will need to present a look consistent with the colours and style of the logo.

Target Market(s)

Business owners

Industry/Entity Type

Accounting/Bookkeeping

Coding

Coded - Design and coding required

Number of Pages Required

1 page

```html
<!DOCTYPE html>
<html lang="en">
<head>
<meta charset="utf-8">
<title>Ledgerly Bookkeeping</title>
<link rel="stylesheet" href="https://fonts.googleapis.com/css2?family=Poppins:wght@400;500;600;700;800&display=swap">
<style>
:root{
  --green:#7cc520;
  --green-soft:#e9f6d8;
  --blue:#1aa7dd;
  --orange:#f7a21b;
  --ink:#1f1f24;
  --text:#5b5e66;
  --muted:#9a9ca3;
  --line:#e6e7ea;
  --grey-band:#f3f4f6;
  --dark:#17181c;
  --white:#ffffff;
}
*{margin:0;padding:0;box-sizing:border-box}
html,body{width:1200px;height:4360px;overflow:hidden}
body{font-family:'Poppins',sans-serif;color:var(--ink);background:var(--white);position:relative}
.abs{position:absolute}
.btn{display:inline-block;border-radius:20px;font-size:11px;font-weight:600;letter-spacing:.5px;color:var(--white);padding:9px 22px;text-transform:uppercase;white-space:nowrap}
.btn-blue{background:var(--blue)}
.btn-dark{background:var(--ink)}
.btn-green{background:var(--green)}
.btn-orange{background:var(--orange)}
.art{position:absolute;border-radius:18px}
.eyebrow{color:var(--green);font-weight:700;font-size:15px;text-transform:uppercase;letter-spacing:.5px}
.body-copy{font-size:13px;line-height:1.65;color:var(--text)}

/* header */
.site-header{top:0;left:0;width:1200px;height:70px}
.brand{left:40px;top:14px;display:flex;align-items:center;gap:10px;font-weight:800;font-size:20px;color:var(--ink)}
.brand-mark{width:30px;height:30px;background:var(--green);border-radius:6px}
.main-nav{right:40px;top:22px;display:flex;align-items:center;gap:26px;font-size:11px;font-weight:600;text-transform:uppercase}
.nav-cta{border:1.5px solid var(--blue);border-radius:16px;padding:6px 14px;color:var(--ink)}

/* hero */
.hero-title{left:80px;top:285px;font-size:44px;font-weight:700;line-height:1.15;width:560px}
.hero-copy{left:80px;top:400px;width:440px}
.hero-btn{left:80px;top:462px}
.hero-art{left:580px;top:60px;width:580px;height:620px;background:radial-gradient(circle at 55% 55%,#dff2c4 0%,#eef8e2 55%,#ffffff 80%)}

/* services */
.services{top:790px;left:150px;width:920px;display:flex;justify-content:space-between}
.service{width:200px;text-align:center;font-size:14px;font-weight:600;line-height:1.4}
.service svg{display:block;margin:0 auto 14px}

/* about */
.grey-wave{left:0;top:1090px}
.about-art{left:100px;top:980px;width:470px;height:370px;background:linear-gradient(160deg,#f4f4f6,#e3f2cf)}
.about-text{left:620px;top:1050px;width:470px}
.section-title{font-size:38px;font-weight:700;line-height:1.15;margin:6px 0 14px}

/* team */
.team-text{left:180px;top:1720px;width:390px}
.team-art{left:620px;top:1660px;width:480px;height:360px;background:linear-gradient(200deg,#f3f3f5,#dcefbf)}

/* pricing */
.pricing-head{top:2140px;left:0;width:1200px;text-align:center}
.pricing-head .section-title{font-size:34px}
.features{left:90px;top:2306px;width:320px}
.features h4{font-size:16px;font-weight:700;margin-bottom:10px}
.row{height:22px;font-size:11px;color:var(--ink);display:flex;align-items:center;white-space:nowrap}
.row.bold{font-weight:700}
.plan{top:2260px;width:160px;height:530px;background:var(--white);border-radius:10px;box-shadow:0 8px 28px rgba(0,0,0,.09);text-align:center}
.plan-head{height:80px;padding-top:14px}
.plan-small{font-size:11px;color:var(--muted)}
.plan-name{font-size:26px;font-weight:800;line-height:1.2}
.plan .row{justify-content:center;color:var(--text)}
.plan .btn{margin-top:14px;padding:7px 16px;font-size:10px}

/* team cards */
.experts-title{top:2880px;left:0;width:1200px;text-align:center;font-size:34px;font-weight:700}
.card{top:2960px;width:240px;height:280px;background:var(--white);box-shadow:0 6px 22px rgba(0,0,0,.08);border-radius:6px;text-align:center;overflow:hidden}
.card-photo{height:165px;background:linear-gradient(180deg,#eceef1,#d7dade)}
.card h5{font-size:15px;font-weight:700;margin-top:12px}
.card .role{font-size:10px;color:var(--muted);text-transform:uppercase}
.card p{font-size:10px;color:var(--text);margin:6px 30px 0;line-height:1.5}
.slider-dot{top:3390px;width:34px;height:34px;border-radius:50%;background:var(--grey-band);display:flex;align-items:center;justify-content:center}

/* cta + footer */
.footer-bg{left:0;top:3700px}
.cta{left:100px;top:3620px;width:1010px;height:300px;background:var(--green);border-radius:14px;text-align:center;color:var(--white);padding-top:56px}
.cta h2{font-size:32px;font-weight:700;line-height:1.25}
.cta p{font-size:12px;opacity:.9;margin:12px auto 24px;width:560px;line-height:1.6}
.footer-brand{left:90px;top:4050px;display:flex;align-items:center;gap:10px;color:var(--white);font-weight:800;font-size:22px}
.footer-brand .brand-mark{width:40px;height:40px}
.fcol{top:4030px;color:var(--white)}
.fcol h6{font-size:16px;font-weight:700;margin-bottom:12px}
.fcol li{list-style:none;font-size:12px;color:#c9cacd;margin-bottom:9px;display:flex;align-items:center;gap:8px;white-space:nowrap}
.copyright{left:90px;top:4318px;font-size:11px;color:#c9cacd}
.socials{right:90px;top:4320px;display:flex;gap:10px}
.socials span{width:12px;height:12px;border-radius:50%;background:#c9cacd}
</style>
</head>
<body>

<header class="abs site-header">
  <div class="abs brand"><span class="brand-mark"></span>Ledgerly</div>
  <nav class="abs main-nav">
    <span>About Us</span><span>Our Team</span><span>Pricing</span><span>Contact</span>
    <span class="nav-cta">Start a Conversation</span>
  </nav>
</header>

<section>
  <div class="art hero-art" role="img" aria-label="Illustration of a person working on a laptop in a green bean bag with money coins and a rising chart"></div>
  <h1 class="abs hero-title">Accounting Technology, Bookkeeping Services</h1>
  <p class="abs hero-copy body-copy">From bookkeeping to tax filing, Ledgerly is the all-in-one financial toolkit your business can count on.</p>
  <span class="abs hero-btn btn btn-blue">Get Started</span>
</section>

<section class="abs services">
  <div class="service">
    <svg width="56" height="56" viewBox="0 0 56 56" fill="none" stroke="var(--ink)" stroke-width="2"><rect x="8" y="12" width="32" height="36" rx="3"/><path d="M14 22h20M14 30h20M14 38h12"/><circle cx="42" cy="16" r="9" fill="var(--green)" stroke="none"/></svg>
    Accounting Advisory &amp; Bookkeeping
  </div>
  <div class="service">
    <svg width="56" height="56" viewBox="0 0 56 56" fill="none" stroke="var(--ink)" stroke-width="2"><circle cx="28" cy="28" r="16"/><circle cx="28" cy="28" r="6" fill="var(--green)" stroke="none"/><path d="M28 6v6M28 44v6M6 28h6M44 28h6"/></svg>
    Accounting Technology Integration
  </div>
  <div class="service">
    <svg width="56" height="56" viewBox="0 0 56 56" fill="none" stroke="var(--ink)" stroke-width="2"><rect x="6" y="14" width="44" height="30" rx="3"/><path d="M14 36l9-9 7 6 12-12"/><circle cx="42" cy="21" r="4" fill="var(--green)" stroke="none"/></svg>
    Strategic Financial Management
  </div>
  <div class="service">
    <svg width="56" height="56" viewBox="0 0 56 56" fill="none" stroke="var(--ink)" stroke-width="2"><rect x="10" y="8" width="30" height="40" rx="3"/><path d="M16 18h18M16 26h18M16 34h10"/><circle cx="40" cy="38" r="8" fill="var(--green)" stroke="none"/></svg>
    Pre-Audit Review Preparation
  </div>
</section>

<svg class="abs grey-wave" width="1200" height="480" viewBox="0 0 1200 480"><path d="M0 60C300 0 700 120 1200 30V420C800 480 400 380 0 440Z" fill="var(--grey-band)"/></svg>

<section>
  <div class="art about-art" role="img" aria-label="Illustration of financial papers with pie charts and graphs spread on a desk"></div>
  <div class="abs about-text">
    <div class="eyebrow">About Us</div>
    <h2 class="section-title">We support all<br>bookkeeping Services</h2>
    <p class="body-copy">Lorem ipsum is simply dummy text of the printing and typesetting industry. Lorem ipsum has been the industry's standard dummy text ever since the 1500s, when an unknown printer took a galley of type and scrambled it to make a type specimen book. It has survived not only five centuries.</p>
    <span class="btn btn-blue" style="margin-top:16px">Read More</span>
  </div>
</section>

<section>
  <div class="abs team-text">
    <div class="eyebrow">Our Team</div>
    <h2 class="section-title" style="font-size:34px">Connect with a<br>Dedicated Team</h2>
    <p class="body-copy">Lorem ipsum is simply dummy text of the printing and typesetting industry. Lorem ipsum has been the industry's standard dummy text ever since the 1500s, when an unknown printer took a galley of type and scrambled it to make a type specimen.</p>
    <span class="btn btn-blue" style="margin-top:16px">Read More</span>
  </div>
  <div class="art team-art" role="img" aria-label="Illustration of two business people shaking hands in front of puzzle pieces with charts"></div>
</section>

<section>
  <div class="abs pricing-head">
    <div class="eyebrow">Pricing Plans</div>
    <h2 class="section-title">Affordable Pricing Plans</h2>
  </div>

  <div class="abs features">
    <h4>Features:</h4>
    <div class="row">Dedicated account manager</div>
    <div class="row">Bank/Card accounts</div>
    <div class="row">Account reconciliation</div>
    <div class="row">BAS</div>
    <div class="row">IAS</div>
    <div class="row">TPAR</div>
    <div class="row">Monthly performance report</div>
    <div class="row">Quarterly performance review (up to 30 mins online)</div>
    <div class="row">Included unlimited email and phone support</div>
    <div class="row">Entering assets in the register/setting up depreciation</div>
    <div class="row">Entering bills</div>
    <div class="row">Monthly aged payables</div>
    <div class="row">Monthly aged receivables</div>
    <div class="row">Included employees for payroll</div>
    <div class="row">Accounts payable included</div>
    <div class="row">Accounts receivable included</div>
    <div class="row">Total value</div>
    <div class="row bold">$AUD value per week (savings*)</div>
  </div>

  <div class="abs plan" style="left:420px">
    <div class="plan-head"><div class="plan-small">Starter</div><div class="plan-name">Lite</div></div>
    <div class="row">1</div><div class="row">2</div><div class="row">Monthly</div><div class="row">✓</div><div class="row">✓</div><div class="row">–</div><div class="row">✓</div><div class="row">–</div><div class="row">Email only</div><div class="row">–</div><div class="row">✓</div><div class="row">✓</div><div class="row">✓</div><div class="row">–</div><div class="row">✓</div><div class="row">✓</div><div class="row">$120</div><div class="row">$35</div>
    <span class="btn btn-dark">Purchase Now</span>
  </div>
  <div class="abs plan" style="left:590px">
    <div class="plan-head"><div class="plan-name" style="color:var(--green);margin-top:10px">Premier</div></div>
    <div class="row">2</div><div class="row">4</div><div class="row">Weekly</div><div class="row">✓</div><div class="row">✓</div><div class="row">✓</div><div class="row">✓</div><div class="row">✓</div><div class="row">✓</div><div class="row">✓</div><div class="row">✓</div><div class="row">✓</div><div class="row">✓</div><div class="row">1–3 (Saving $15)</div><div class="row">✓</div><div class="row">✓</div><div class="row">$265</div><div class="row">$60</div>
    <span class="btn btn-blue">Purchase Now</span>
  </div>
  <div class="abs plan" style="left:760px">
    <div class="plan-head"><div class="plan-small">Business</div><div class="plan-name">Core</div></div>
    <div class="row">3</div><div class="row">6</div><div class="row">Daily</div><div class="row">✓</div><div class="row">✓</div><div class="row">✓</div><div class="row">✓</div><div class="row">✓</div><div class="row">✓</div><div class="row">✓</div><div class="row">✓</div><div class="row">✓</div><div class="row">✓</div><div class="row">4–6 (Saving $70)</div><div class="row">✓</div><div class="row">✓</div><div class="row">$480</div><div class="row">$96</div>
    <span class="btn btn-green">Purchase Now</span>
  </div>
  <div class="abs plan" style="left:930px">
    <div class="plan-head"><div class="plan-small">Boss</div><div class="plan-name" style="color:var(--orange)">Elite</div></div>
    <div class="row">Unlimited</div><div class="row">Unlimited</div><div class="row">Daily</div><div class="row">✓</div><div class="row">✓</div><div class="row">✓</div><div class="row">✓</div><div class="row">✓</div><div class="row">✓</div><div class="row">✓</div><div class="row">✓</div><div class="row">✓</div><div class="row">✓</div><div class="row">7–10 (Saving $90)</div><div class="row">✓</div><div class="row">✓</div><div class="row">$570</div><div class="row">$125</div>
    <span class="btn btn-orange">Purchase Now</span>
  </div>
</section>

<section>
  <h2 class="abs experts-title">Meet With Experth</h2>
  <div class="abs card" style="left:105px">
    <div class="card-photo" role="img" aria-label="Portrait photo of a team member"></div>
    <h5>Owen Halbrook</h5><div class="role">Designer</div>
    <p>Lorem ipsum dolor sit amet, consectetur adipiscing elit sed do eiusmod.</p>
  </div>
  <div class="abs card" style="left:355px">
    <div class="card-photo" role="img" aria-label="Portrait photo of a team member"></div>
    <h5>Rafael Montero</h5><div class="role">Manager</div>
    <p>Lorem ipsum dolor sit amet, consectetur adipiscing elit sed do eiusmod.</p>
  </div>
  <div class="abs card" style="left:605px">
    <div class="card-photo" role="img" aria-label="Portrait photo of a team member"></div>
    <h5>Daniel Corvina</h5><div class="role">Founder</div>
    <p>Lorem ipsum dolor sit amet, consectetur adipiscing elit sed do eiusmod.</p>
  </div>
  <div class="abs card" style="left:855px">
    <div class="card-photo" role="img" aria-label="Portrait photo of a team member"></div>
    <h5>Daniel Corvina</h5><div class="role">Director</div>
    <p>Lorem ipsum dolor sit amet, consectetur adipiscing elit sed do eiusmod.</p>
  </div>
  <div class="abs slider-dot" style="left:560px"><svg width="12" height="12" viewBox="0 0 12 12" fill="none" stroke="var(--ink)" stroke-width="1.6"><path d="M8 2L4 6l4 4"/></svg></div>
  <div class="abs slider-dot" style="left:606px"><svg width="12" height="12" viewBox="0 0 12 12" fill="none" stroke="var(--ink)" stroke-width="1.6"><path d="M4 2l4 4-4 4"/></svg></div>
</section>

<footer>
  <svg class="abs footer-bg" width="1200" height="660" viewBox="0 0 1200 660"><path d="M0 110C250 30 500 40 700 70S1050 60 1200 0V660H0Z" fill="var(--dark)"/></svg>
  <div class="abs cta">
    <h2>Join thousands of small business<br>owners who trust Ledgerly with their books</h2>
    <p>Get started today and let our expert team keep your accounts accurate, current and ready so you can focus on growing your business.</p>
    <span class="btn btn-dark">Start a Free Trial</span>
  </div>

  <div class="abs footer-brand"><span class="brand-mark"></span>Ledgerly</div>
  <div class="abs fcol" style="left:520px"><h6>Quick Links</h6><ul><li>About Us</li><li>Our Team</li><li>Pricing</li><li>Contact</li></ul></div>
  <div class="abs fcol" style="left:720px"><h6>Useful Links</h6><ul><li>Privacy Policy</li><li>Terms and Conditions</li><li>Disclaimer</li><li>Support</li><li>FAQ</li></ul></div>
  <div class="abs fcol" style="left:920px"><h6>Contact</h6><ul>
    <li><svg width="10" height="12" viewBox="0 0 10 12" fill="var(--green)"><path d="M5 0a4 4 0 0 1 4 4c0 3-4 8-4 8S1 7 1 4a4 4 0 0 1 4-4z"/></svg>Some great address here</li>
    <li><svg width="12" height="10" viewBox="0 0 12 10" fill="none" stroke="var(--green)"><rect x=".5" y=".5" width="11" height="9"/><path d="M.5 .5l5.5 5 5.5-5"/></svg>info@ledgerly.example</li>
    <li><svg width="11" height="11" viewBox="0 0 11 11" fill="var(--green)"><path d="M2 0l2 2.5-1 1.5a7 7 0 0 0 4 4l1.5-1L11 9l-2 2C4 11 0 7 0 2z"/></svg>+1 (555) 014 2290</li>
    <li><svg width="11" height="11" viewBox="0 0 11 11" fill="none" stroke="var(--green)"><circle cx="5.5" cy="5.5" r="5"/><path d="M.5 5.5h10M5.5 .5c2 2 2 8 0 10M5.5 .5c-2 2-2 8 0 10"/></svg>www.ledgerly.example</li>
  </ul></div>
  <div class="abs copyright">©Copyright 2020 | All Rights Reserved</div>
  <div class="abs socials"><span></span><span></span><span></span><span></span></div>
</footer>

</body>
</html>
```